Salmon Shop that sells both wholesale and retail salmon in a variety of ways.

"Harbour Fillet Co" is a business that is selling atlantic salmon in every way possible. We will be a salmon butcher to the public for retail purchase and we will also be out and about trying to sell our products to restaurants cafes and any other wholesale way. Our product is from Tasmania but we will be trading on the Sunshine Coast. The shop design has an urban, rustic feel and very much about the product. One of the owners has worked on salmon farms for 15 years and we want it to be very specialised and quality. I have nothing to offer you to help with this design....I would like both a salmon on the card, not sure if image or silohette is best and would like the other side to have a fillet with a tag of some sort. We are looking for a logo also. Use a photo of an Atlantic Salmon, Atlantic Salmon have two fins along the back.
Updates

Project Deadline Extended Reason: I am extending the deadline as I have still not got exactly what I want. All designers have added something great to what I am after and I just need someone to pull it all together. I have put in a new brief with a sketched image to help so we can get this perfect. Please read all the instructions. Thank you Added Monday, February 16, 2015

Target Market(s)

Restaurants, cafes

Industry/Entity Type

Retail

Contact Information for Business Card

Harbour Fillet Co (Not to have "Shop" at the end.Shop 12/130-164 Brisbane RdMooloolaba 4557

Colors
1c66ab

Requirements
Must have
• logo for harbour fillet Co with the S being salmon fillet of fresh salmon on white platemap of tasmaniasepia /black and white image of atlantic salmon
Nice to have
• fillet of salmonmap of tasmaniasalmon
Should not have
• Not Shop at the end.

```html
<!DOCTYPE html>
<html lang="en">
<head>
<meta charset="utf-8">
<title>Harbour Fillet Co — Business Card</title>
<link rel="stylesheet" href="https://fonts.googleapis.com/css2?family=Oswald:wght@400;500;600&display=swap">
<style>
  :root {
    --page: #ffffff;
    --paper: #dcc9a8;
    --paper-light: #e6d6ba;
    --paper-dark: #cfb993;
    --ink: #2a211a;
    --salmon: #ea5a2a;
    --sepia-dark: #3e3024;
    --sepia-mid: #7d6a55;
    --sepia-light: #b9a586;
  }
  * { margin: 0; padding: 0; box-sizing: border-box; }
  html, body {
    width: 963px;
    height: 1200px;
    overflow: hidden;
    background: var(--page);
  }
  .sheet {
    position: relative;
    width: 963px;
    height: 1200px;
  }
  .card {
    position: absolute;
    left: 53px;
    width: 858px;
    height: 532px;
    overflow: hidden;
    background:
      radial-gradient(ellipse at 30% 20%, var(--paper-light), transparent 60%),
      radial-gradient(ellipse at 80% 90%, var(--paper-dark), transparent 65%),
      var(--paper);
  }
  .card--front { top: 48px; }
  .card--back { top: 624px; }

  .salmon-photo {
    position: absolute;
    left: -75px;
    top: 184px;
    width: 640px;
    height: 156px;
    border-radius: 50% 45% 45% 50% / 50%;
    transform: rotate(-48deg);
    background: linear-gradient(180deg, var(--sepia-dark) 0%, var(--sepia-mid) 40%, var(--sepia-light) 100%);
    opacity: 0.85;
  }

  .brand {
    position: absolute;
    display: flex;
    align-items: center;
  }
  .brand__name {
    font-family: "Oswald", sans-serif;
    font-weight: 600;
    color: var(--salmon);
    text-transform: uppercase;
    text-align: right;
    letter-spacing: 1px;
  }
  .brand__mark {
    flex: none;
    border-radius: 50%;
    background: var(--salmon);
  }

  .card--front .brand { right: 42px; top: 200px; gap: 24px; }
  .card--front .brand__name { font-size: 84px; line-height: 88px; }
  .card--front .brand__mark { width: 112px; height: 112px; }

  .card--back .brand { left: 60px; top: 60px; gap: 18px; }
  .card--back .brand__name { font-size: 52px; line-height: 54px; }
  .card--back .brand__mark { width: 64px; height: 64px; }

  .address {
    position: absolute;
    left: 462px;
    top: 158px;
    font-family: "Oswald", sans-serif;
    font-weight: 500;
    font-size: 30px;
    line-height: 42px;
    color: var(--ink);
    letter-spacing: 1px;
    font-variant: small-caps;
  }
  .divider {
    position: absolute;
    left: 51px;
    top: 264px;
    width: 775px;
    height: 4px;
    background: var(--ink);
  }
  .contact {
    position: absolute;
    left: 0;
    right: 0;
    top: 336px;
    text-align: center;
    font-family: "Oswald", sans-serif;
    color: var(--ink);
  }
  .contact__name {
    font-weight: 600;
    font-size: 56px;
    line-height: 64px;
    text-transform: uppercase;
    letter-spacing: 2px;
  }
  .contact__phone {
    font-weight: 600;
    font-size: 46px;
    line-height: 54px;
    letter-spacing: 3px;
  }
</style>
</head>
<body>
  <main class="sheet">
    <section class="card card--front">
      <div class="salmon-photo" role="img" aria-label="Sepia photograph of a leaping Atlantic salmon"></div>
      <div class="brand">
        <p class="brand__name">Harbour<br>Fillet<br>Co</p>
        <span class="brand__mark" aria-hidden="true"></span>
      </div>
    </section>

    <section class="card card--back">
      <div class="brand">
        <p class="brand__name">Harbour<br>Fillet<br>Co</p>
        <span class="brand__mark" aria-hidden="true"></span>
      </div>
      <p class="address">Shop 7/210-236 Wattlebay Rd<br>Kirrawee 4812</p>
      <div class="divider"></div>
      <div class="contact">
        <p class="contact__name">Ben</p>
        <p class="contact__phone">812345670</p>
      </div>
    </section>
  </main>
</body>
</html>
```